Illustrations for a Project Management Concept

we need illustrations for 5 project management principles that make up a holistic approach to project management, without all the BS. if we extract all the methodology, system, tool and mumbo-jumbo out of project management, we end up with some essential principles that are simple to understand and use. It's likely that people who use them will not be traditional Project Management types.

I've mocked up something that looks very corporate based on a template, but this has the wrong tone; the wrong feeling. I'd like something "funky" and colorful that conveys "Action" within "Simplicity".

the PPT file with the dark-blue background is the "corporate" consulting type mockup. the PPT with the white background shows an idea I had for breaking out each of the 5 principles (only one shown) to make it larger, with some text in a callout.

In the final deliverable, I need to be able to both show all 5 on one diagram, as well as slicing the image to display each principle separately. i do not have editing capabilities for vector image formats, only image formats

Reason: there are a number of designers who have only just accepted the invitation. I want to give everyone a chance to submit.

```html
<!DOCTYPE html>
<html lang="en">
<head>
<meta charset="utf-8">
<title>5 Project Action Principles for Successful Project Management</title>
<link rel="stylesheet" href="https://fonts.googleapis.com/css2?family=PT+Sans:wght@400;700&family=PT+Sans+Narrow&display=swap">
<style>
  :root {
    --title: #3b5660;
    --label: #3a3a3a;
    --note: #7d7d7d;
    --rule: #4a4a4a;
    --blue: #2f9bd6;
    --blue-light: #9fd0ef;
    --gray: #8d8f92;
    --gray-dark: #6e7073;
    --green: #86b83a;
    --green-light: #c8e08e;
    --orange: #f07d1e;
    --orange-light: #fac89a;
    --red: #e6222a;
    --red-light: #f0594c;
    --accent-blue: #2f9bd6;
    --accent-green: #8cc63f;
    --accent-orange: #f08a24;
    --accent-red: #e6222a;
    --bg-top: #c6c7c9;
    --bg-bottom: #ffffff;
  }
  * { box-sizing: border-box; margin: 0; padding: 0; }
  html, body { width: 1200px; height: 1007px; overflow: hidden; }
  body {
    position: relative;
    background: linear-gradient(180deg, var(--bg-top) 0%, #e6e7e8 45%, var(--bg-bottom) 80%);
    font-family: "PT Sans", sans-serif;
  }
  .title {
    position: absolute;
    top: 24px; left: 0; width: 1200px;
    text-align: center;
    font-weight: 400;
    font-size: 50px;
    line-height: 58px;
    color: var(--title);
    letter-spacing: 0.2px;
  }
  .diagram { position: absolute; inset: 0; width: 1200px; height: 1007px; }
  .principle-label { font-family: "PT Sans", sans-serif; font-size: 19px; fill: var(--label); text-anchor: middle; }
  .principle-adverb { font-size: 19px; text-anchor: middle; }
  .principle-number { font-family: "PT Sans", sans-serif; font-weight: 700; font-size: 38px; fill: #fff; text-anchor: middle; }
  .note {
    position: absolute;
    font-family: "PT Sans Narrow", sans-serif;
    font-size: 10.5px;
    line-height: 12.6px;
    color: var(--note);
  }
  .note--right { text-align: right; }
  .note-outcomes { left: 160px; top: 229px; width: 280px; }
  .note-value { left: 868px; top: 250px; width: 250px; }
  .note-models { left: 1026px; top: 575px; width: 162px; }
  .note-entropy { left: 60px; top: 603px; width: 214px; }
  .note-teaming { left: 630px; top: 861px; width: 358px; }
</style>
</head>
<body>
  <h1 class="title">5 Project Action Principles for Successful Project<br>Management</h1>

  <svg class="diagram" viewBox="0 0 1200 1007" xmlns="http://www.w3.org/2000/svg">
    <defs>
      <polygon id="octagon" points="-0.4142,-1 0.4142,-1 1,-0.4142 1,0.4142 0.4142,1 -0.4142,1 -1,0.4142 -1,-0.4142"/>
      <linearGradient id="fill-blue" x1="0" y1="0" x2="0" y2="1">
        <stop offset="0.55" stop-color="var(--blue)"/>
        <stop offset="1" stop-color="var(--blue-light)"/>
      </linearGradient>
      <linearGradient id="fill-gray" x1="0" y1="0" x2="1" y2="1">
        <stop offset="0" stop-color="#a3a5a8"/>
        <stop offset="1" stop-color="var(--gray-dark)"/>
      </linearGradient>
      <linearGradient id="fill-green" x1="0" y1="0" x2="1" y2="0">
        <stop offset="0.45" stop-color="var(--green)"/>
        <stop offset="1" stop-color="var(--green-light)"/>
      </linearGradient>
      <linearGradient id="fill-orange" x1="0" y1="0" x2="1" y2="0">
        <stop offset="0" stop-color="var(--orange-light)"/>
        <stop offset="0.45" stop-color="var(--orange)"/>
      </linearGradient>
      <linearGradient id="fill-red" x1="0" y1="0" x2="0" y2="1">
        <stop offset="0" stop-color="var(--red-light)"/>
        <stop offset="0.45" stop-color="var(--red)"/>
      </linearGradient>
      <radialGradient id="fill-face" cx="0.5" cy="0.45" r="0.6">
        <stop offset="0.4" stop-color="#ffffff"/>
        <stop offset="1" stop-color="#c4c6c8"/>
      </radialGradient>
      <filter id="lift" x="-20%" y="-20%" width="140%" height="140%">
        <feDropShadow dx="0" dy="4" stdDeviation="5" flood-color="#000" flood-opacity="0.28"/>
      </filter>
    </defs>

    <!-- connector rules -->
    <g class="connectors" stroke="var(--rule)" stroke-width="1" fill="none">
      <polyline points="445,229 445,296 570,420"/>
      <polyline points="861,252 861,328 845,328"/>
      <polyline points="1018,575 1018,590 996,612"/>
      <polyline points="278,590 278,725"/>
      <polyline points="622,818 646,830 646,928"/>
    </g>

    <!-- principle 2 -->
    <g class="principle principle-value" filter="url(#lift)">
      <use href="#octagon" transform="translate(708 299) scale(151)" fill="url(#fill-blue)"/>
      <use href="#octagon" transform="translate(708 298) scale(102)" fill="url(#fill-face)"/>
      <text class="principle-label" x="703" y="246">Fulfill Customer</text>
      <text class="principle-label" x="703" y="269">Value</text>
      <text class="principle-adverb" x="703" y="296" fill="var(--accent-blue)">Interactively</text>
      <g class="icon-touch" fill="var(--accent-blue)">
        <circle cx="698" cy="324" r="11" fill="none" stroke="var(--accent-blue)" stroke-width="2.5"/>
        <circle cx="698" cy="324" r="5"/>
        <rect x="694" y="324" width="8" height="20" rx="4"/>
        <path d="M690 340 h24 a4 4 0 0 1 4 4 v10 a14 14 0 0 1 -14 14 h-4 a12 12 0 0 1 -12 -12 v-12 a4 4 0 0 1 2 -4z"/>
      </g>
      <text class="principle-number" x="818" y="301">2</text>
    </g>

    <!-- principle 5 -->
    <g class="principle principle-entropy" filter="url(#lift)">
      <use href="#octagon" transform="translate(325 447) scale(143)" fill="url(#fill-green)"/>
      <use href="#octagon" transform="translate(326 446) scale(97)" fill="url(#fill-face)"/>
      <text class="principle-label" x="325" y="406">Suppress Project</text>
      <text class="principle-label" x="325" y="430">Entropy</text>
      <text class="principle-adverb" x="325" y="457" fill="var(--accent-green)">Selectively</text>
      <g class="icon-search" fill="none" stroke="var(--accent-green)" stroke-width="3">
        <rect x="302" y="478" width="46" height="44" rx="7"/>
        <circle cx="329" cy="496" r="8"/>
        <line x1="323" y1="502" x2="312" y2="513" stroke-linecap="round"/>
        <circle cx="335" cy="509" r="4" fill="var(--accent-green)" stroke="none"/>
      </g>
      <text class="principle-number" x="207" y="461">5</text>
    </g>

    <!-- principle 3 -->
    <g class="principle principle-models" filter="url(#lift)">
      <use href="#octagon" transform="translate(855 665) scale(142)" fill="url(#fill-orange)"/>
      <use href="#octagon" transform="translate(855 664) scale(97)" fill="url(#fill-face)"/>
      <text class="principle-label" x="855" y="613">Build Shared</text>
      <text class="principle-label" x="855" y="637">Models</text>
      <text class="principle-adverb" x="855" y="665" fill="var(--accent-orange)">Verifiably</text>
      <g class="icon-check" fill="none" stroke="var(--accent-orange)" stroke-width="3">
        <rect x="834" y="686" width="42" height="42" rx="6"/>
        <polyline points="843,707 852,716 868,698" stroke-width="4.5" stroke-linecap="round" stroke-linejoin="round"/>
      </g>
      <text class="principle-number" x="970" y="676">3</text>
    </g>

    <!-- principle 4 -->
    <g class="principle principle-teaming" filter="url(#lift)">
      <use href="#octagon" transform="translate(482 820) scale(142)" fill="url(#fill-red)"/>
      <use href="#octagon" transform="translate(482 819) scale(97)" fill="url(#fill-face)"/>
      <text class="principle-label" x="482" y="781">Eliminate Teaming</text>
      <text class="principle-label" x="482" y="804">Threats</text>
      <text class="principle-label" x="482" y="831">Ruthlessly</text>
      <g class="icon-path" fill="none" stroke="var(--accent-red)" stroke-width="5" stroke-linecap="round">
        <path d="M463 878 v6 a6 6 0 0 0 12 0 v-24 a9 9 0 0 1 18 0 v2"/>
        <circle cx="463" cy="872" r="3.5" fill="var(--accent-red)" stroke="none"/>
        <circle cx="476" cy="862" r="3.5" fill="var(--accent-red)" stroke="none"/>
        <path d="M501 862 v14" />
        <circle cx="501" cy="879" r="3.5" fill="var(--accent-red)" stroke="none"/>
      </g>
      <text class="principle-number" x="603" y="831">4</text>
    </g>

    <!-- principle 1 -->
    <g class="principle principle-outcomes" filter="url(#lift)">
      <use href="#octagon" transform="translate(590 553) scale(137)" fill="url(#fill-gray)"/>
      <use href="#octagon" transform="translate(590 552) scale(100)" fill="url(#fill-face)"/>
      <text class="principle-label" x="590" y="510">Achieve Outcomes</text>
      <text class="principle-adverb" x="590" y="543" fill="var(--accent-blue)">Rapidly</text>
      <g class="icon-stopwatch" fill="none" stroke="#3c3c3c">
        <rect x="583" y="558" width="14" height="8" rx="2" fill="#3c3c3c" stroke="none"/>
        <rect x="579" y="553" width="22" height="6" rx="2" fill="#3c3c3c" stroke="none"/>
        <rect x="618" y="566" width="9" height="12" rx="2" fill="#3c3c3c" stroke="none" transform="rotate(40 622 572)"/>
        <circle cx="590" cy="605" r="36" stroke-width="7"/>
        <g stroke-width="3" stroke-linecap="round">
          <line x1="590" y1="576" x2="590" y2="581"/>
          <line x1="590" y1="629" x2="590" y2="634"/>
          <line x1="561" y1="605" x2="566" y2="605"/>
          <line x1="614" y1="605" x2="619" y2="605"/>
          <line x1="571" y1="586" x2="574" y2="589"/>
          <line x1="609" y1="586" x2="606" y2="589"/>
          <line x1="571" y1="624" x2="574" y2="621"/>
          <line x1="609" y1="624" x2="606" y2="621"/>
          <line x1="590" y1="605" x2="576" y2="592" stroke-width="4"/>
        </g>
        <circle cx="590" cy="605" r="4" fill="#3c3c3c" stroke="none"/>
      </g>
      <text class="principle-number" x="714" y="574">1</text>
    </g>
  </svg>

  <p class="note note--right note-outcomes">Consciously and deliberately focus on the achievement of outcomes over the execution of tasks and activities. Outcomes deliver projects, but not all tasks result in outcomes. And move as quickly as the situation allows. Everything else flows from this principle.</p>

  <p class="note note-value">Any activity, resource investment, or outcome that does not service a customer value proposition is waste and probably avoidable. The definition of value must be obtained directly from the customer, not an intermediary. Project deliverables must be validated with customers repeatedly and directly.</p>

  <p class="note note-models">Use vivid and graphic models for all project concepts, and constantly validate and update those models. Invest time to share and align these models with project participants. Constantly refer to the models to embed them into everyone's planning and thinking, forming a resilient master-plan for project outcomes.</p>

  <p class="note note--right note-entropy">Trust the implementation and guidance of the first 4 project action principles to significantly reduce the entropy in your project. For the remaining entropic events, selectively invest time only where the result will materially improve the achievement of project outcomes. Do not attempt to implement comprehensive entropy control processes.</p>

  <p class="note note-teaming">Trust and allow the first three principles to provide the environment for self-teaming and collaboration to naturally occur, instead of forcing popularised team-building processes. Invest your time to identify and eliminate teaming threats that would negatively impact the self-creation of the team.</p>
</body>
</html>
```